Marrow Business Cards

Front of business card will have logo, name, address, & telephone number. Back of card will have a list of services provided - Roads, Substation Pads, Temporary Pads, Site Pads, Land Leveling, Powerline Row Cleaning, Land Clearing, Gates, Fencing, Construction Entrances, Excavation, Trenching, Underground Utilities, Directional Boring, Pile Driving. We are a construction company that uses heavy equipment like bulldozers, motor graders/blades, dump trucks, backhoes, hydro axes, & skid loaders. We build roads, pads, & install electric utility lines & waterlines underground. This logo is new. The word "Construction" can be smaller as uploaded 2 example edited logos. We will be using this card design for many employees.
Target Market(s)
Industrial Electric Powerline, Wind Turbine, Solar Panel, & Water Utility companies.
Contact Information for Business Card
Name/Position - Dorian Quale - Owner
Address: 4837 FM 582
Tarrow, TX 79418
Phone number - (325) 418-2906

```html
<!DOCTYPE html>
<html lang="en">
<head>
<meta charset="utf-8">
<title>Marrow Construction Business Cards</title>
<link rel="stylesheet" href="https://fonts.googleapis.com/css2?family=Arimo:wght@400;700&display=swap">
<style>
  :root {
    --maroon: #3a1017;
    --paper: #ffffff;
    --ink-grey: #3c3c3c;
    --rule: #b9b9b9;
    --backdrop: #d9d9d9;
    --on-maroon: #f4f1f1;
  }
  * { margin: 0; padding: 0; box-sizing: border-box; }
  html, body {
    width: 1200px;
    height: 802px;
    overflow: hidden;
    background: var(--backdrop);
    font-family: "Arimo", Arial, sans-serif;
  }
  .stage {
    position: relative;
    width: 1200px;
    height: 802px;
  }
  .card {
    position: absolute;
    top: 274px;
    width: 443px;
    height: 264px;
  }
  .card--front { left: 136px; background: var(--paper); }
  .card--back { left: 608px; background: var(--maroon); color: var(--on-maroon); }

  /* front */
  .brand {
    position: absolute;
    left: 28px;
    top: 100px;
    width: 190px;
    text-align: center;
    color: var(--maroon);
    font-weight: 700;
  }
  .brand__name { font-size: 38px; line-height: 1; letter-spacing: 0.5px; }
  .brand__sub { font-size: 19px; line-height: 1; margin-top: 38px; letter-spacing: 0.5px; }
  .divider {
    position: absolute;
    left: 235px;
    top: 75px;
    width: 2px;
    height: 123px;
    background: var(--rule);
  }
  .contact {
    position: absolute;
    left: 250px;
    top: 77px;
    color: var(--ink-grey);
  }
  .contact__name { font-size: 16px; font-weight: 700; color: var(--maroon); line-height: 1.1; }
  .contact__role { font-size: 12px; line-height: 1.3; }
  .contact__phone { font-size: 18px; margin-top: 18px; }
  .contact__address { font-size: 14px; line-height: 1.45; margin-top: 14px; }

  /* back */
  .brand--back {
    position: absolute;
    left: 0;
    right: 0;
    top: 72px;
    text-align: center;
    font-size: 44px;
    font-weight: 700;
    letter-spacing: 1px;
    color: var(--on-maroon);
    line-height: 1;
  }
  .services {
    position: absolute;
    left: 40px;
    right: 40px;
    top: 168px;
    text-align: center;
    font-size: 12.6px;
    line-height: 19.5px;
  }
</style>
</head>
<body>
<main class="stage">
  <section class="card card--front" aria-label="Business card front">
    <div class="brand">
      <div class="brand__name">MARROW</div>
      <div class="brand__sub">CONSTRUCTION</div>
    </div>
    <div class="divider"></div>
    <div class="contact">
      <p class="contact__name">DORIAN QUALE</p>
      <p class="contact__role">OWNER</p>
      <p class="contact__phone">(325) 418-2906</p>
      <p class="contact__address">4837 FM 582<br>Tarrow, TX 79418</p>
    </div>
  </section>

  <section class="card card--back" aria-label="Business card back">
    <div class="brand--back">MARROW</div>
    <p class="services">Roads | Substation Pads | Temporary Pads | Site Pads | Land Leveling, Powerline Row Cleaning | Land Clearing | Gates Fencing | Construction Entrances | Excavation | Trenching Underground Utilities | Directional Boring | Pile Driving.</p>
  </section>
</main>
</body>
</html>
```